IT Services company general flyer

Looking for a printable US letter size flyer to give a brief overview of the services we offer. We also partner with another company for their services as well. Please check out our website at www.gearbymarlon.com and click on "Our Services" to learn about our services and visit www.bluepinesafety,com and click on services to learn about their services. Several of our services do overlap, so they only need to be on the flyer once. Let me know if this is too much content and we need to weed some out. We do not want Home phone service on this flyer. The basic design of the flyer should mimic similar to the VOIP one you did for me for the colors and logo. Also check out the "Who Choose us" page on www.gearbymarlon.com to include some of that as well.
Updates

Gathering more feedback

Target Market(s)

Targeting Small businesses that may not normally have a budget for their IT Services

Industry/Entity Type

It Service

Font styles to use
Serif
Sans Serif

Requirements
Must have
• Must include my logo, phone number and email/website address and must follow the same basic template of my previous flyers.

```html
<!DOCTYPE html>
<html lang="en">
<head>
<meta charset="utf-8">
<title>Gear by Marlon – IT Services Flyer</title>
<link href="https://fonts.googleapis.com/css2?family=Roboto:wght@400;700&family=Barlow:wght@600&display=swap" rel="stylesheet">
<style>
  :root {
    --backdrop: #6b7f7b;
    --paper: #ffffff;
    --navy: #14246b;
    --navy-deep: #0d1a55;
    --blue-mid: #1f4c9a;
    --blue-light: #3f78c8;
    --red: #8b0a0a;
    --white: #ffffff;
    --rule: rgba(255,255,255,0.75);
  }
  * { margin: 0; padding: 0; box-sizing: border-box; }
  html, body { width: 1200px; height: 750px; overflow: hidden; }
  body { background: var(--backdrop); position: relative; font-family: 'Roboto', sans-serif; }

  .flyer {
    position: absolute; left: 364px; top: 42px;
    width: 470px; height: 665px;
    background: var(--paper); overflow: hidden;
  }

  .flyer-header { position: absolute; left: 0; top: 0; width: 470px; height: 104px; background: var(--paper); }
  .brand-mark {
    position: absolute; left: 40px; top: 34px; width: 34px; height: 34px;
    background: var(--navy);
  }
  .brand-divider { position: absolute; left: 113px; top: 18px; width: 1px; height: 80px; background: #c8c8c8; }
  .brand-name {
    position: absolute; left: 124px; top: 30px;
    font-family: 'Barlow', sans-serif; font-weight: 600; color: var(--navy);
    font-size: 27px; line-height: 24px; letter-spacing: -0.5px;
  }

  .hero-image {
    position: absolute; left: 0; top: 104px; width: 470px; height: 516px;
    background:
      radial-gradient(ellipse at 78% 40%, rgba(130,180,240,0.55) 0%, rgba(60,110,190,0.2) 30%, transparent 55%),
      radial-gradient(ellipse at 65% 60%, rgba(190,150,130,0.35) 0%, transparent 35%),
      linear-gradient(100deg, var(--blue-mid) 0%, #1a3f86 45%, #1c2c52 75%, #2a3348 100%);
  }

  .services { position: absolute; left: 0; top: 0; width: 470px; }
  .service { position: absolute; left: 73px; width: 143px; color: var(--white); }
  .service-title { font-weight: 700; font-size: 10.5px; line-height: 13px; margin-bottom: 1px; white-space: nowrap; }
  .service-text { font-size: 8.6px; line-height: 11.4px; }
  .service-rule { position: absolute; left: 74px; width: 142px; height: 1px; background: var(--rule); }
  .service-icon { position: absolute; left: 40px; width: 30px; height: 30px; }

  .footer-visit {
    position: absolute; left: 0; top: 621px; width: 119px; height: 15px;
    background: var(--navy); clip-path: polygon(0 0, 113px 0, 119px 15px, 0 15px);
    color: var(--white); font-size: 6.5px; line-height: 15px; padding-left: 20px;
  }
  .visit-square { display: inline-block; width: 7px; height: 7px; background: var(--white); vertical-align: -1px; margin-left: 6px; }
  .footer-web {
    position: absolute; left: 0; top: 636px; width: 306px; height: 29px;
    background: var(--red); color: var(--white);
    font-size: 12.5px; letter-spacing: 2px; line-height: 29px; padding-left: 20px;
  }
  .footer-contact-panel {
    position: absolute; left: 288px; top: 620px; width: 182px; height: 45px;
    background: var(--navy-deep); clip-path: polygon(14px 0, 182px 0, 182px 45px, 0 45px);
  }
  .contact-tab {
    position: absolute; left: 216px; top: 622px; width: 88px; height: 15px;
    background: var(--white); clip-path: polygon(5px 0, 88px 0, 83px 15px, 0 15px);
    color: #111; font-size: 10px; font-weight: 400; text-align: center; line-height: 15px; letter-spacing: 0.3px;
  }
  .contact-phone {
    position: absolute; left: 323px; top: 624px; color: var(--white);
    font-weight: 700; font-size: 16.5px; line-height: 18px;
  }
  .contact-phone svg { vertical-align: -2px; margin-right: 4px; }
  .contact-email {
    position: absolute; left: 322px; top: 644px; color: var(--white);
    font-size: 8.8px; line-height: 12px;
  }
  .contact-email svg { vertical-align: -1px; margin-right: 7px; }
</style>
</head>
<body>
  <div class="flyer">
    <header class="flyer-header">
      <span class="brand-mark"></span>
      <span class="brand-divider"></span>
      <div class="brand-name">GEAR<br>BY MARLON</div>
    </header>

    <div class="hero-image" role="img" aria-label="Photo of a businessman in a suit touching a glowing digital interface with tech icons, binary code and a world map"></div>

    <section class="services">
      <svg class="service-icon" style="top:158px" viewBox="0 0 30 30" fill="none" stroke="#fff" stroke-width="1.6">
        <rect x="6" y="4" width="18" height="6" rx="1"/><rect x="6" y="12" width="18" height="6" rx="1"/>
        <path d="M5 27h20a4 4 0 0 0-2-7 6 6 0 0 0-11-1 4 4 0 0 0-7 8z" fill="#fff"/>
      </svg>
      <div class="service" style="top:140px">
        <div class="service-title">Managed IT Service</div>
        <div class="service-text">You need your IT systems for your day to day work. Let us help manage and protect them.</div>
      </div>
      <div class="service-rule" style="top:191px"></div>

      <svg class="service-icon" style="top:252px" viewBox="0 0 30 30" fill="#fff">
        <path d="M8 4c1.5 0 3 3 3.5 5s-1.5 2.5-2 3.5c1.2 3 3 5 6 6.5 1-.5 1.8-2.5 3.5-2s5 2 5 3.5-2 5-4.5 5C12 25.5 4.5 18 4.5 9 4.5 6 6.5 4 8 4z"/>
      </svg>
      <div class="service" style="top:227px">
        <div class="service-title">Business VOIP Phone Service</div>
        <div class="service-text">Reduce cost and improve commu-nication for your business. Solutions available for any size business from 1 phone to hundreds of phones.</div>
      </div>
      <div class="service-rule" style="top:291px"></div>

      <svg class="service-icon" style="top:350px" viewBox="0 0 30 30" fill="none" stroke="#fff" stroke-width="1.8">
        <rect x="6" y="13" width="14" height="12" rx="1.5" fill="#fff"/><path d="M9 13V9a4 4 0 0 1 8 0v4"/>
        <circle cx="23" cy="20" r="4"/>
      </svg>
      <div class="service" style="top:328px">
        <div class="service-title">Network Security</div>
        <div class="service-text">Worried about the latest ransom-ware or crypto virus? We can help design and protect your network.</div>
      </div>
      <div class="service-rule" style="top:380px"></div>

      <svg class="service-icon" style="top:448px" viewBox="0 0 30 30" fill="none" stroke="#fff" stroke-width="2.4" stroke-linecap="round">
        <path d="M3 11a17 17 0 0 1 24 0"/><path d="M7.5 15.5a11 11 0 0 1 15 0"/><path d="M11.5 19.5a5 5 0 0 1 7 0"/>
        <circle cx="15" cy="24" r="1.6" fill="#fff" stroke="none"/>
      </svg>
      <div class="service" style="top:417px">
        <div class="service-title">Wireless Solutions</div>
        <div class="service-text">Is your wireless coverage spotty or would you like to extend your network or internet coverage to another building?</div>
      </div>
      <div class="service-rule" style="top:480px"></div>

      <svg class="service-icon" style="top:535px" viewBox="0 0 30 30" fill="#fff">
        <path d="M6 19h19a5 5 0 0 0-3-9 7 7 0 0 0-13-1 5 5 0 0 0-3 10z"/>
        <path d="M15 19v5M9 24h12" stroke="#fff" stroke-width="1.6"/>
        <circle cx="8" cy="25" r="2.5"/><circle cx="22" cy="25" r="2.5"/>
      </svg>
      <div class="service" style="top:506px">
        <div class="service-title">Cloud Services</div>
        <div class="service-text">Want your own business email service? Want to move to the cloud for secure file storage and sharing? Ask us about our complete cloud</div>
      </div>
      <div class="service-rule" style="top:570px"></div>
    </section>

    <div class="footer-visit">VISIT US AT<span class="visit-square"></span></div>
    <div class="footer-web">www.gearbymarlon.com</div>
    <div class="footer-contact-panel"></div>
    <div class="contact-tab">CONTACT US</div>
    <div class="contact-phone">
      <svg width="14" height="14" viewBox="0 0 16 16" fill="none" stroke="#fff" stroke-width="1.4"><circle cx="8" cy="8" r="7"/><path d="M5.5 4.5c.7 0 1.2 1.3 1.3 2s-.7 1-.8 1.3c.5 1.1 1.2 1.9 2.3 2.4.4-.2.7-.9 1.3-.7s1.8.8 1.8 1.3-.8 1.5-1.6 1.5C6.800 12.300 4.300 9.500 4.300 6.100 4.300 5.200 4.900 4.500 5.500 4.500z" fill="#fff" stroke="none"/></svg>320.555.0147
    </div>
    <div class="contact-email">
      <svg width="10" height="8" viewBox="0 0 10 8"><rect width="10" height="8" rx="1" fill="#fff"/><path d="M0.5 1L5 4.5 9.5 1" fill="none" stroke="#0d1a55" stroke-width="1"/></svg>sales@gearbymarlon.com
    </div>
  </div>
</body>
</html>
```